Business Card For Video Production Company

Please NOTE: I've added some info to the must haves that I should have included at the start. Thank you.

I need a business card design for my video production company based in Orlando called Caldera Film Works. Our work consists of web video marketing (web videos), training videos, sales videos, conference and seminar video production...basically a lot of corporate based work.

We work with successful small businesses, not-for-profits and some Fortune 500 type groups. We bring a lot of knowledge, experience and attention to detail to every project.

I'd like something that communicates strength, confidence, integrity, as well as creative vision. I want to stay away from the standard icons of the media and film industry. I'd like to emphasize the colors of my logo, and also the colors of my website which has a white background. Simple is good.

Our budgets are moderate...generally $1500 to $5000.

www.calderafilm.tv

PS...We don't do weddings or recitals, or that type of production.
Updates

I want to thank all the designers for your updates. There's way too many to be able to give feedback on for all. I hope you understand that. But wow…there are so many great designs everyone has offered. I can't thank you enough…each and everyone. I hope to make my decision soon. I'm not accepting anymore designs from new designers. Brent-

Target Market(s)

Successful small businesses, marketing directors, corporate communication directors, training and human resources professionals. forward thinking not-for profits. Since my company is based in Central Florida, most of my work comes from this area too.

Industry/Entity Type

Marketing

Requirements
Must have
• website address, www.calderafilm.tv
phone number, 407-552-9031
email address, brent@calderafilm.tv

Title
Brent Caldera
Owner/Creative Director

I'd like to have a single line that goes across illustrating our services, maybe separated with bullet points:

Marketing Videos, Corporate Videos, Conference & Seminar Video Production
Should not have
• No film or video icons.
No need to pull language or copy from my website.

```html
<!DOCTYPE html>
<html lang="en">
<head>
<meta charset="utf-8">
<title>Caldera Film Works — Business Card</title>
<link rel="stylesheet" href="https://fonts.googleapis.com/css2?family=Oswald:wght@300;400;500&display=swap">
<style>
  :root {
    --backdrop: #e6e7e9;
    --card-white: #ffffff;
    --brand-blue: #175d94;
    --accent-blue: #8fd0f2;
    --ink-dark: #3a3d42;
    --shadow: rgba(0, 0, 0, 0.18);
  }
  * { margin: 0; padding: 0; box-sizing: border-box; }
  html, body {
    width: 1200px;
    height: 913px;
    overflow: hidden;
    background: var(--backdrop);
    font-family: "Oswald", "Arial Narrow", sans-serif;
  }
  .sheet {
    width: 1200px;
    height: 913px;
    display: flex;
    align-items: center;
    justify-content: center;
    gap: 40px;
  }
  .card {
    width: 540px;
    height: 309px;
    position: relative;
    box-shadow: 0 10px 28px var(--shadow);
  }

  /* Front */
  .card--front {
    background: var(--card-white);
    display: flex;
    align-items: center;
    justify-content: center;
    gap: 16px;
  }
  .brand-square {
    width: 44px;
    height: 44px;
    background: var(--brand-blue);
  }
  .brand-name {
    font-size: 40px;
    font-weight: 500;
    color: var(--ink-dark);
    letter-spacing: 0.5px;
  }

  /* Back */
  .card--back {
    background: var(--brand-blue);
    color: var(--accent-blue);
    padding: 30px 40px;
  }
  .services {
    font-size: 13px;
    font-weight: 300;
    letter-spacing: 0.4px;
    font-style: normal;
  }
  .identity {
    position: absolute;
    left: 40px;
    top: 118px;
    text-transform: uppercase;
    line-height: 1.05;
  }
  .identity__name,
  .identity__title {
    font-size: 27px;
    font-weight: 400;
    letter-spacing: 0.4px;
  }
  .divider {
    position: absolute;
    left: 40px;
    top: 194px;
    width: 260px;
    height: 1.5px;
    background: var(--accent-blue);
  }
  .contacts {
    position: absolute;
    left: 40px;
    top: 206px;
    list-style: none;
    font-size: 14px;
    font-weight: 300;
    line-height: 24px;
  }
  .contacts li {
    display: flex;
    align-items: center;
    gap: 6px;
  }
  .contacts svg {
    width: 12px;
    height: 12px;
    fill: none;
    stroke: var(--accent-blue);
    stroke-width: 1.6;
  }
</style>
</head>
<body>
  <main class="sheet">
    <section class="card card--front" aria-label="Card front">
      <span class="brand-square" aria-hidden="true"></span>
      <span class="brand-name">Caldera Film Works</span>
    </section>

    <section class="card card--back" aria-label="Card back">
      <p class="services">• Marketing Videos • Corporate Videos • Conference &amp; Seminar Video</p>

      <div class="identity">
        <p class="identity__name">Brent Caldera</p>
        <p class="identity__title">Owner • Creative Director</p>
      </div>

      <span class="divider" aria-hidden="true"></span>

      <ul class="contacts">
        <li>
          <svg viewBox="0 0 12 12" aria-hidden="true"><circle cx="6" cy="6" r="5"/><path d="M1 6h10M6 1c2 2 2 8 0 10M6 1c-2 2-2 8 0 10"/></svg>
          <span>: Calderafilm.tv</span>
        </li>
        <li>
          <svg viewBox="0 0 12 12" aria-hidden="true"><rect x="1" y="2.5" width="10" height="7"/><path d="M1 2.5l5 4 5-4"/></svg>
          <span>: Brent@calderafilm.tv</span>
        </li>
        <li>
          <svg viewBox="0 0 12 12" aria-hidden="true"><path d="M3 1h2l1 3-1.5 1a6 6 0 0 0 2.5 2.5L8 6l3 1v2a2 2 0 0 1-2 2A8 8 0 0 1 1 3a2 2 0 0 1 2-2z"/></svg>
          <span>: 407.552.9031</span>
        </li>
      </ul>
    </section>
  </main>
</body>
</html>
```